Scientific project description

Here is a project description related to cellular mechanics, showing above the forces acting on cells in the tissues of our body. The forces on single cells are there to depict how forces are acting on cells (pressure squeezes the cell, shear flow is pushing the upward parts of the cell, tension pulls one part of the cell, strain is stretching the whole cell; the single cell images are to be found also on the last page). Intense red/purple are used to indicate that the forces are stressful (the colors to be used do not need to be exactly like these colors). The picture in the middle is a view of cells (same picture on next page if that needs to be modified). At the left, a description of what happens when everything is going well, i.e. the body stays healthy. At the right, if you dysfunction you get disease. Green nuances were used to indicate health, brownish, perhaps not so pleasant nuances were used to indicate disease. Below are the steps of the project.

On the whole, we're rather happy with the concept description as such, but it should look a little bit nicer. To many color nuances give a "noisy" impression, fonts could be nicer, layout more crisp, and the text on the steps should be more readable. We would also like to have two versions of the same picture, one with black background, one with white.

Target Market(s)

Scientists that are evaluating our project

Requirements
Must have
• Easy to grasp the idea, easy to read and understand the underlying idea.
Nice to have
• Would be good to have the Concept title ("Vorlix Concept and Envisioned Project Progression) on top of the figure as indicated in the second brief picture submitted.

```html
<!DOCTYPE html>
<html lang="en">
<head>
<meta charset="utf-8">
<title>Vorlix Concept and Envisioned Project Progression</title>
<link href="https://fonts.googleapis.com/css2?family=Oswald:wght@400;500;600&display=swap" rel="stylesheet">
<style>
  :root {
    --stage: #9a9a9a;
    --arrow-red: #ff1a1a;
    --health-green: #7cc21f;
    --disease-blue: #4a9ccc;
    --step-text: #1a1a1a;
    --cell-tan: #d8c4a0;
  }
  html, body {
    margin: 0;
    padding: 0;
    width: 1195px;
    height: 1200px;
    overflow: hidden;
    background: var(--stage);
    font-family: "Oswald", "Arial Narrow", sans-serif;
  }
  .canvas { position: relative; width: 1195px; height: 1200px; }
  .panel { position: absolute; left: 222px; width: 743px; height: 551px; }
  .panel--dark { top: 44px; --panel-bg: #000; --title-ink: #fff; }
  .panel--light { top: 616px; --panel-bg: #fff; --title-ink: #000; }
  .panel svg { display: block; width: 743px; height: 551px; }
  .panel__bg { fill: var(--panel-bg); }
  .panel__title { fill: var(--title-ink); font-size: 35px; font-weight: 500; }
  .force-box { fill: url(#forceGradient); }
  .force-label { fill: #fff; font-size: 22px; font-weight: 500; }
  .force-arrow { stroke: #fff; stroke-width: 2.5; fill: none; }
  .cell-figure { fill: var(--cell-tan); }
  .flow-arrow { stroke: var(--arrow-red); stroke-width: 11; fill: none; }
  .core { fill: url(#coreGradient); }
  .core-glow { fill: none; stroke: var(--health-green); stroke-opacity: 0.35; stroke-width: 8; }
  .core-label { fill: #fff; font-size: 34px; font-weight: 500; }
  .state-circle--health { fill: var(--health-green); }
  .state-circle--disease { fill: var(--disease-blue); }
  .state-circle__text { fill: #fff; font-size: 19px; font-weight: 400; }
  .link-text--health { fill: var(--health-green); font-size: 22px; }
  .link-text--disease { fill: var(--disease-blue); font-size: 22px; }
  .link--health { stroke: var(--health-green); stroke-width: 8; fill: none; }
  .link--disease { stroke: var(--disease-blue); stroke-width: 8; fill: none; }
  .outcome--health { fill: var(--health-green); font-size: 34px; font-weight: 500; }
  .outcome--disease { fill: var(--disease-blue); font-size: 34px; font-weight: 500; }
  .icon-slot--health { fill: var(--health-green); }
  .icon-slot--disease { fill: var(--disease-blue); }
  .step { fill: url(#stepGradient); }
  .step-label { fill: var(--step-text); font-size: 13px; font-weight: 400; }
</style>
</head>
<body>
<div class="canvas">

  <section class="panel panel--dark">
    <svg viewBox="0 0 928 689" aria-label="Vorlix concept diagram, dark version">
      <defs>
        <linearGradient id="forceGradient" x1="0" y1="0" x2="0" y2="1">
          <stop offset="0" stop-color="#c40808"/>
          <stop offset="0.5" stop-color="#f01616"/>
          <stop offset="1" stop-color="#e21010"/>
        </linearGradient>
        <radialGradient id="coreGradient" cx="0.5" cy="0.5" r="0.5">
          <stop offset="0" stop-color="#1e3f18"/>
          <stop offset="0.7" stop-color="#2f6a22"/>
          <stop offset="1" stop-color="#0c1a0c"/>
        </radialGradient>
        <linearGradient id="stepGradient" x1="0" y1="0" x2="0" y2="1">
          <stop offset="0" stop-color="#fafafa"/>
          <stop offset="1" stop-color="#c4c4c4"/>
        </linearGradient>
        <marker id="redHead" markerUnits="userSpaceOnUse" markerWidth="34" markerHeight="34" refX="6" refY="17" orient="auto">
          <path d="M0 0 L34 17 L0 34 Z" fill="#ff1a1a"/>
        </marker>
        <marker id="greenHead" markerUnits="userSpaceOnUse" markerWidth="22" markerHeight="26" refX="4" refY="13" orient="auto">
          <path d="M0 0 L22 13 L0 26 Z" fill="#7cc21f"/>
        </marker>
        <marker id="greenDown" markerUnits="userSpaceOnUse" markerWidth="20" markerHeight="22" refX="4" refY="11" orient="auto">
          <path d="M0 0 L20 11 L0 22 Z" fill="#7cc21f"/>
        </marker>
        <marker id="blueDown" markerUnits="userSpaceOnUse" markerWidth="20" markerHeight="22" refX="4" refY="11" orient="auto">
          <path d="M0 0 L20 11 L0 22 Z" fill="#4a9ccc"/>
        </marker>
        <marker id="whiteHead" markerUnits="userSpaceOnUse" markerWidth="10" markerHeight="10" refX="2" refY="5" orient="auto">
          <path d="M0 0 L10 5 L0 10 Z" fill="#fff"/>
        </marker>
      </defs>
      <g id="conceptDiagram">
        <rect class="panel__bg" width="928" height="689"/>
        <text class="panel__title" x="455" y="50" text-anchor="middle">Vorlix CONCEPT AND ENVISIONED PROJECT PROGRESSION</text>

        <g class="force force--pressure">
          <rect class="force-box" x="67" y="70" width="182" height="119"/>
          <text class="force-label" x="158" y="97" text-anchor="middle">PRESSURE</text>
          <line class="force-arrow" marker-end="url(#whiteHead)" x1="115" y1="106" x2="115" y2="126"/>
          <line class="force-arrow" marker-end="url(#whiteHead)" x1="136" y1="110" x2="136" y2="130"/>
          <line class="force-arrow" marker-end="url(#whiteHead)" x1="157" y1="113" x2="157" y2="133"/>
          <line class="force-arrow" marker-end="url(#whiteHead)" x1="178" y1="110" x2="178" y2="130"/>
          <line class="force-arrow" marker-end="url(#whiteHead)" x1="199" y1="106" x2="199" y2="126"/>
          <rect class="cell-figure" role="img" aria-label="Cell squeezed flat by pressure" x="97" y="148" width="122" height="26" rx="13"/>
        </g>
        <g class="force force--shear">
          <rect class="force-box" x="265" y="70" width="181" height="119"/>
          <text class="force-label" x="360" y="97" text-anchor="middle">SHEAR</text>
          <line class="force-arrow" marker-end="url(#whiteHead)" x1="293" y1="135" x2="313" y2="135"/>
          <line class="force-arrow" marker-end="url(#whiteHead)" x1="320" y1="127" x2="340" y2="127"/>
          <line class="force-arrow" marker-end="url(#whiteHead)" x1="347" y1="119" x2="367" y2="119"/>
          <rect class="cell-figure" role="img" aria-label="Cell pushed sideways by shear flow" x="300" y="140" width="124" height="34" rx="17"/>
        </g>
        <g class="force force--tension">
          <rect class="force-box" x="462" y="70" width="181" height="119"/>
          <text class="force-label" x="552" y="97" text-anchor="middle">TENSION</text>
          <line class="force-arrow" marker-end="url(#whiteHead)" x1="534" y1="137" x2="534" y2="117"/>
          <line class="force-arrow" marker-end="url(#whiteHead)" x1="553" y1="128" x2="553" y2="106"/>
          <line class="force-arrow" marker-end="url(#whiteHead)" x1="572" y1="137" x2="572" y2="117"/>
          <rect class="cell-figure" role="img" aria-label="Cell pulled upward by tension" x="490" y="142" width="124" height="32" rx="16"/>
        </g>
        <g class="force force--strain">
          <rect class="force-box" x="660" y="70" width="181" height="119"/>
          <text class="force-label" x="750" y="97" text-anchor="middle">STRAIN</text>
          <rect class="cell-figure" role="img" aria-label="Cell stretched lengthwise by strain" x="695" y="144" width="110" height="14" rx="7"/>
          <line class="force-arrow" marker-end="url(#whiteHead)" x1="708" y1="145" x2="680" y2="145"/>
          <line class="force-arrow" marker-end="url(#whiteHead)" x1="708" y1="158" x2="680" y2="158"/>
          <line class="force-arrow" marker-end="url(#whiteHead)" x1="792" y1="145" x2="820" y2="145"/>
          <line class="force-arrow" marker-end="url(#whiteHead)" x1="792" y1="158" x2="820" y2="158"/>
        </g>

        <path class="flow-arrow" marker-end="url(#redHead)" d="M212 198 Q250 255 312 265"/>
        <path class="flow-arrow" marker-end="url(#redHead)" d="M354 198 Q372 215 378 225"/>
        <path class="flow-arrow" marker-end="url(#redHead)" d="M555 198 Q538 215 532 225"/>
        <path class="flow-arrow" marker-end="url(#redHead)" d="M698 198 Q660 255 598 265"/>

        <circle class="core-glow" cx="455" cy="352" r="121"/>
        <circle class="core" role="img" aria-label="Fluorescence microscopy view of cells" cx="455" cy="352" r="117"/>
        <text class="core-label" x="455" y="364" text-anchor="middle" textLength="205" lengthAdjust="spacingAndGlyphs">MECHANOSTASIS</text>

        <path class="link--health" marker-end="url(#greenHead)" d="M325 348 H248"/>
        <text class="link-text--health" x="278" y="334" text-anchor="middle">CELL</text>
        <text class="link-text--health" x="278" y="381" text-anchor="middle">FITNESS</text>
        <circle class="state-circle--health" cx="139" cy="348" r="72"/>
        <text class="state-circle__text" x="139" y="329" text-anchor="middle">FUNCTIONAL</text>
        <text class="state-circle__text" x="139" y="357" text-anchor="middle">CELLULAR</text>
        <text class="state-circle__text" x="139" y="385" text-anchor="middle">MACHINERIES</text>
        <path class="link--health" stroke-width="5" marker-end="url(#greenDown)" d="M139 433 V458"/>
        <rect class="icon-slot--health" role="img" aria-label="Weightlifter pictogram" x="95" y="488" width="88" height="82" rx="6"/>
        <text class="outcome--health" x="135" y="614" text-anchor="middle">HEALTH</text>

        <path class="link--disease" d="M600 348 H680 M600 336 V360"/>
        <text class="link-text--disease" x="635" y="334" text-anchor="middle">CELL</text>
        <text class="link-text--disease" x="635" y="381" text-anchor="middle">FRAILTY</text>
        <circle class="state-circle--disease" cx="768" cy="348" r="72"/>
        <text class="state-circle__text" x="768" y="329" text-anchor="middle">DYSFUNCTIONAL</text>
        <text class="state-circle__text" x="768" y="357" text-anchor="middle">CELLULAR</text>
        <text class="state-circle__text" x="768" y="385" text-anchor="middle">MACHINERIES</text>
        <path class="link--disease" stroke-width="5" marker-end="url(#blueDown)" d="M768 433 V458"/>
        <rect class="icon-slot--disease" role="img" aria-label="Patient and nurse pictogram" x="722" y="488" width="82" height="80" rx="6"/>
        <text class="outcome--disease" x="769" y="614" text-anchor="middle">DISEASE</text>

        <rect class="step" x="377" y="485" width="158" height="20"/>
        <text class="step-label" x="456" y="500" text-anchor="middle">PREVENTION &amp; THERAPIES</text>
        <rect class="step" x="367" y="508" width="177" height="22"/>
        <text class="step-label" x="456" y="524" text-anchor="middle">CRITICAL TARGETS</text>
        <rect class="step" x="358" y="533" width="195" height="24"/>
        <text class="step-label" x="456" y="550" text-anchor="middle">CELLULAR MACHINERIES</text>
        <rect class="step" x="347" y="560" width="217" height="27"/>
        <text class="step-label" x="456" y="578" text-anchor="middle">DISEASE MODELS</text>
        <rect class="step" x="336" y="591" width="239" height="30"/>
        <text class="step-label" x="456" y="611" text-anchor="middle">CELL, TISSUE &amp; ORGAN RESPONSES</text>
        <rect class="step" x="324" y="625" width="263" height="37"/>
        <text class="step-label" x="456" y="648" text-anchor="middle">MECHANICAL FORCE MODELS</text>
      </g>
    </svg>
  </section>

  <section class="panel panel--light">
    <svg viewBox="0 0 928 689" aria-label="Vorlix concept diagram, light version">
      <use href="#conceptDiagram"/>
    </svg>
  </section>

</div>
</body>
</html>
```